Tallbrook Advisory Group LLC Business Card Design

I'm looking for a fresh, sharp, clean and current/modern format for my company. This is a start up in the professional services (security/risk management consulting) industry. Catering to C-suite executives as well as senior director types of larkwood 900 companies.

Target Market(s)

Larkwood 900 companies and their C-suite staff with particular focus on VP of Human Resources and Director of Security.

Industry/Entity Type

Business

Font styles to use
Serif

Colors
0455a3
9bcb3c
acd037
3377b5
eaf1f7

Requirements
Must have
• Fresh, sharp, clean and current/modern look and feel.

```html
<!DOCTYPE html>
<html lang="en">
<head>
<meta charset="utf-8">
<title>Tallbrook Advisory Group – Business Card</title>
<link rel="stylesheet" href="https://fonts.googleapis.com/css2?family=Fira+Sans+Condensed:wght@600&display=swap">
<style>
  :root {
    --navy: #1f2a5c;
    --green: #74a843;
    --paper: #ffffff;
    --backdrop: #e8e9e9;
  }
  * { margin: 0; padding: 0; box-sizing: border-box; }
  html, body {
    width: 1200px;
    height: 1000px;
    overflow: hidden;
    background: var(--backdrop);
  }
  .business-card {
    position: absolute;
    left: 322px;
    top: 318px;
    width: 586px;
    height: 315px;
    background: var(--paper);
    overflow: hidden;
  }
  .card-edges {
    position: absolute;
    inset: 0;
  }
  .edge-navy { fill: var(--navy); }
  .edge-green { fill: var(--green); }
  .brand {
    position: absolute;
    left: 161px;
    top: 128px;
    display: flex;
    align-items: center;
    gap: 32px;
    font-family: "Fira Sans Condensed", sans-serif;
    font-weight: 600;
  }
  .brand-dot {
    width: 70px;
    height: 70px;
    border-radius: 50%;
    background: var(--navy);
    flex: none;
  }
  .brand-text {
    display: flex;
    flex-direction: column;
    width: 164px;
  }
  .brand-name {
    color: var(--navy);
    line-height: 1;
  }
  .brand-name-main {
    display: block;
    font-size: 33px;
    letter-spacing: 0;
  }
  .brand-name-sub {
    display: block;
    font-size: 13.5px;
    letter-spacing: 3.1px;
    margin-top: 3px;
    white-space: nowrap;
  }
  .tagline {
    display: flex;
    align-items: center;
    gap: 4px;
    margin-top: 6px;
    color: var(--green);
    font-size: 10.5px;
    letter-spacing: 0.6px;
    white-space: nowrap;
  }
  .tagline::before,
  .tagline::after {
    content: "";
    flex: 1;
    min-width: 10px;
    height: 1px;
    background: var(--green);
  }
</style>
</head>
<body>
  <div class="business-card">
    <svg class="card-edges" viewBox="0 0 586 315" width="586" height="315" aria-hidden="true">
      <path class="edge-navy" d="M0 0 H28 Q14 170 98 315 H0 Z"/>
      <path class="edge-green" d="M28 0 H108 Q21 158 98 315 Q14 170 28 0 Z"/>
      <path class="edge-navy" d="M586 0 H560 Q571 180 490 315 H586 Z"/>
      <path class="edge-green" d="M478 0 H560 Q571 180 490 315 Q560 160 478 0 Z"/>
    </svg>

    <div class="brand">
      <div class="brand-dot"></div>
      <div class="brand-text">
        <div class="brand-name">
          <span class="brand-name-main">TALLBROOK</span>
          <span class="brand-name-sub">ADVISORY GROUP</span>
        </div>
        <div class="tagline">STEADY, SOUND &amp; CLEAR</div>
      </div>
    </div>
  </div>
</body>
</html>
```